Organic skincare label - minimalist, earthy, luxe design needed!

I need a label design for a luxury natural skin care line called "Velka Botanix". Velka means 'earth' in Swahili. I would like the design to embody an earthy feel but be minimalistic and give a luxe vibe. My first product will be a Tumeric and Neem Scrub.

The size of the jar is 8oz, label dimensions should be (1.625" Tall x 8.5" Wide)
I will be making other products too such as; oils + toners so I feel free to do labels for glass bottles and/or spray bottles as well.

Forest green, light pinks/nudes/beige, grey, white, gold, are colors that can be used (not all have to be used).

I have included pictures of some things I've worked on myself as well as my original logo design but I need to simplify the logo, no circle around it.
Feel free to get creative.

Thank you! :)
Updates

Target Market(s)

Socially Conscious, Beauty Enthusiast, Minimalist

Industry/Entity Type

Skin Care

Font styles to use
Sans Serif
Other font styles liked:
• "Wonderlove doodle" is the font used for "Velka" in the logo. Feel free to use that or change it as you see fit.

Requirements
Must have
• Simplistic design
would like to stick to a font close to the ones in the logo. Either the one used for the name "Velka" OR the one that the slogan "Rooted Rituals" uses.

I have also included some pictures to capture the aesthetic of my social media and website.

Gender neutral

```html
<!DOCTYPE html>
<html lang="en">
<head>
<meta charset="utf-8">
<title>Velka Botanix – Tumeric and Neem Scrub Label</title>
<link href="https://fonts.googleapis.com/css2?family=Montserrat:wght@500&family=Poppins:wght@500&family=Sacramento&display=swap" rel="stylesheet">
<style>
  :root {
    --backdrop: #d6d6d6;
    --label: #f3f3f3;
    --ink: #111111;
  }
  * { margin: 0; padding: 0; box-sizing: border-box; }
  html, body {
    width: 1200px;
    height: 1200px;
    overflow: hidden;
    background: var(--backdrop);
  }
  .canvas {
    width: 1200px;
    height: 1200px;
    display: flex;
    align-items: center;
    justify-content: center;
  }
  .label {
    width: 1040px;
    height: 600px;
    background: var(--label);
    position: relative;
    display: flex;
    flex-direction: column;
    align-items: center;
    padding-top: 66px;
  }
  .label__rule {
    position: absolute;
    left: 0;
    right: 0;
    height: 4px;
    background: var(--ink);
  }
  .label__rule--top { top: 0; }
  .label__rule--bottom { bottom: 0; }
  .brand {
    display: flex;
    align-items: center;
    gap: 14px;
    height: 50px;
  }
  .brand__mark {
    width: 14px;
    height: 14px;
    background: var(--ink);
  }
  .brand__name {
    font-family: "Montserrat", sans-serif;
    font-weight: 500;
    font-size: 34px;
    color: var(--ink);
    line-height: 1;
  }
  .tagline {
    font-family: "Montserrat", sans-serif;
    font-weight: 500;
    font-size: 23px;
    letter-spacing: 3px;
    color: var(--ink);
    margin-top: 10px;
  }
  .product-name {
    font-family: "Poppins", sans-serif;
    font-weight: 500;
    font-size: 41px;
    letter-spacing: -0.5px;
    color: var(--ink);
    margin-top: 120px;
  }
  .product-divider {
    width: 540px;
    height: 1.5px;
    background: var(--ink);
    margin-top: 18px;
  }
  .claim {
    font-family: "Sacramento", cursive;
    font-size: 48px;
    color: var(--ink);
    margin-top: 20px;
    line-height: 1;
  }
  .size-divider {
    width: 190px;
    border-top: 2px dashed var(--ink);
    margin-top: 18px;
  }
  .size {
    font-family: "Montserrat", sans-serif;
    font-weight: 500;
    font-size: 19px;
    letter-spacing: 1px;
    color: var(--ink);
    margin-top: 14px;
  }
</style>
</head>
<body>
  <main class="canvas">
    <section class="label">
      <div class="label__rule label__rule--top"></div>
      <div class="brand">
        <span class="brand__mark"></span>
        <span class="brand__name">Velka Botanix</span>
      </div>
      <div class="tagline">ROOTED RITUALS</div>
      <h1 class="product-name">TUMERIC AND NEEM SCRUB</h1>
      <div class="product-divider"></div>
      <p class="claim">all natural ingredients</p>
      <div class="size-divider"></div>
      <p class="size">8OZ</p>
      <div class="label__rule label__rule--bottom"></div>
    </section>
  </main>
</body>
</html>
```